Brochure for real estate company

We need the brochure in the attachement re-designed in a consistent way with our website. The text and the structure of the text should not be altered, but addidtional design-elements and other stuff can be added. We're looking for a simple and catchy design as in our website (www.kranich-wohnbau.ch). We need design propositions in file formats where we can always change the text ourselves if that is neccessary later on.

Industry/Entity Type

Real Estate

Font styles to use
Sans Serif

Colors
ec2027
f04a50

```html
<!DOCTYPE html>
<html lang="de">
<head>
<meta charset="utf-8">
<title>Broschüre – Seiten 4 und 5</title>
<link href="https://fonts.googleapis.com/css2?family=Jost:wght@400;500;700&family=PT+Sans:wght@400;700&family=Noto+Serif:wght@400;700&display=swap" rel="stylesheet">
<style>
  :root{
    --stage:#8a8b8a;
    --paper:#ffffff;
    --red:#f04a50;
    --red-strong:#ec2027;
    --ink-dark:#262626;
    --grey-text:#6b6b6b;
    --table-line:#555555;
    --label:#111111;
  }
  *{box-sizing:border-box;margin:0;padding:0}
  html,body{width:1200px;height:1000px;overflow:hidden}
  body{background:var(--stage);position:relative;font-family:"PT Sans",sans-serif}

  .page{position:absolute;top:130px;width:524px;height:740px;background:var(--paper);overflow:hidden}
  .page--four{left:44px}
  .page--five{left:618px;width:523px}

  .page-label{position:absolute;top:890px;width:200px;text-align:center;font-family:"PT Sans",sans-serif;font-size:29px;color:var(--label)}
  .page-label--four{left:208px}
  .page-label--five{left:780px}

  .photo-cut{position:absolute;overflow:hidden}
  .photo-cut .photo{width:100%;border-radius:50%}

  /* page 4 */
  .page--four .photo-cut{top:63px;width:135px;height:127px}
  .page--four .photo{height:135px}
  .photo-garden{background:radial-gradient(circle at 55% 40%,#a9c86a,#4f7a2e 60%,#8b8b7c)}
  .photo-house{background:linear-gradient(180deg,#3f7fd6 0%,#8ab0d8 35%,#c9b36c 48%,#6fae3a 62%,#3f8a24 100%)}
  .photo-loft{background:linear-gradient(160deg,#7a5a3a,#c9a577 45%,#e4dccd 75%,#9e8a70)}

  .intro{position:absolute;left:46px;top:236px;width:450px;font-family:"Jost",sans-serif;font-size:18.5px;line-height:22px;color:var(--grey-text)}

  .band-red{position:absolute;left:0;top:322px;width:100%;height:385px;background:var(--red)}
  .band-dark{position:absolute;left:0;top:707px;width:100%;height:33px;background:var(--ink-dark)}
  .side-curve{position:absolute;top:346px;height:332px;width:28px;background:var(--ink-dark);border-radius:14px}
  .side-curve--left{left:-16px}
  .side-curve--right{right:-16px}

  .section-title{position:absolute;left:0;top:332px;width:100%;text-align:center;font-family:"Jost",sans-serif;font-weight:700;font-size:22.5px;color:#fff}
  .bullet-list{position:absolute;left:46px;width:440px;list-style:none;color:#fff;font-size:10px;line-height:13px}
  .bullet-list li{margin-bottom:9px}
  .bullet-list--services{top:372px}
  .bullet-list--edge{top:526px}
  .bullet-list .tick{margin-right:3px}
  .subhead{position:absolute;left:0;top:498px;width:100%;text-align:center;font-family:"Noto Serif",serif;font-size:13px;color:#fff}
  .subhead strong{font-weight:700}

  /* page 5 */
  .overview-title{position:absolute;left:0;top:60px;width:100%;text-align:center;font-family:"Jost",sans-serif;font-weight:700;font-size:22px;color:var(--red-strong);letter-spacing:.3px}
  .fee-table{position:absolute;left:107px;top:102px;width:296px;border-collapse:collapse;font-family:"Noto Serif",serif;font-size:10px;color:#222;text-align:center}
  .fee-table th,.fee-table td{border:1px solid var(--table-line);height:26px;padding:0 3px;line-height:11px}
  .fee-table th{background:var(--red);color:#fff;font-weight:400;font-size:10.5px;height:30px}
  .fee-table th:first-child{width:138px}
  .fee-table th:nth-child(2){width:78px}
  .fee-table .tall td{height:52px}
  .footnote{position:absolute;left:106px;top:372px;width:304px;font-family:"Noto Serif",serif;font-size:5.2px;line-height:6.6px;color:#222}

  .band-red--five{top:477px;height:106px}
  .page--five .photo-cut{top:410px;width:135px;height:135px}
  .page--five .photo{height:135px}
  .photo-villa{background:linear-gradient(180deg,#4d8fe0 0%,#b9c9d6 30%,#d8c79a 55%,#7fb14a 78%,#5a9632 100%)}
  .photo-attic{background:radial-gradient(circle at 50% 35%,#f3ece4,#d8c4ad 55%,#a8643a 85%)}
  .photo-living{background:linear-gradient(180deg,#5b3a24 0%,#8a5c3a 35%,#6d8e4a 55%,#8d3e2a 100%)}

  .skyline{position:absolute;left:42px;top:600px;width:436px;height:140px;background:linear-gradient(180deg,#ffffff,#d9d9d9);border-radius:2px}
</style>
</head>
<body>

<section class="page page--four">
  <div class="photo-cut" style="left:46px"><div class="photo photo-garden" role="img" aria-label="Foto eines Gartens mit blühendem Strauch vor einem Haus"></div></div>
  <div class="photo-cut" style="left:192px"><div class="photo photo-house" role="img" aria-label="Foto einer Häuserzeile mit Rasen unter blauem Himmel"></div></div>
  <div class="photo-cut" style="left:338px"><div class="photo photo-loft" role="img" aria-label="Foto eines Dachgeschosses mit Holztreppe und Galerie"></div></div>

  <p class="intro">Die rechtliche Sicherheit ist bei einem Immobiliengeschäft für alle Parteien zentral. Wir überlassen nichts dem Zufall – durch unser Wissen sichern wir Sie ab.</p>

  <div class="band-red"></div>
  <div class="side-curve side-curve--left"></div>
  <div class="side-curve side-curve--right"></div>
  <div class="band-dark"></div>

  <h2 class="section-title">Administration &amp; Eigentumsübertrag</h2>
  <ul class="bullet-list bullet-list--services">
    <li><span class="tick">✓</span>Bankgarantie: Kaufwillige Interessenten begleiten wir bis zum unwiderruflichen Zahlungsversprechen der Bank.</li>
    <li><span class="tick">✓</span>Kaufvertrag: Vom vorläufigen Kaufvertragsentwurf bis zum Unterzeichnungstermin kümmern wir uns um alles und beraten die Parteien kompetent.</li>
    <li><span class="tick">✓</span>Besondere Wünsche: Ob Hypothekenübernahme, Absicherung der Anzahlung oder besondere Übernahmemodalitäten, wir sorgen für die korrekte rechtliche Umsetzung.</li>
  </ul>
  <h3 class="subhead"><strong>Klartext:</strong> Das machen wir besser als die Konkurrenz</h3>
  <ul class="bullet-list bullet-list--edge">
    <li><span class="tick">✓</span>Wir arbeiten bis zum Schluss: Viele Makler bemühen sich bis zur Reservationsvereinbarung und lassen sich danach Zeit. Wir betrachten unsere Pflicht erst dann als erfüllt, wenn das Zahlungsversprechen und die notarielle Beurkundung zustanden gekommen sind.</li>
    <li><span class="tick">✓</span>Wir sind vernetzt: Unsere Partnerschaften reichen vom Bankberater bis zum Notar, so stellen wir eine prioritäre Behandlung Ihres Geschäfts sicher.</li>
  </ul>
</section>

<section class="page page--five">
  <h2 class="overview-title">Unsere Leistung im Überblick</h2>
  <table class="fee-table">
    <tr><th>Mandatsart</th><th>Exklusiv</th><th>Nicht-<br>Exklusiv</th></tr>
    <tr><td>Aufschaltgebühr</td><td>Keine</td><td>Keine</td></tr>
    <tr><td>Insertionskosten</td><td>Keine</td><td>Keine</td></tr>
    <tr><td>Reine Erfolgsprovision</td><td>2%</td><td>2.5%</td></tr>
    <tr><td>Mindestprovision</td><td>Keine</td><td>Keine</td></tr>
    <tr><td>Exklusiv</td><td>Ja</td><td>Nein</td></tr>
    <tr><td>Gratis HBV Schätzung*</td><td>Ja</td><td>Ja</td></tr>
    <tr><td>Begleitung Notariat</td><td>Kostenlos</td><td>Kostenlos</td></tr>
    <tr class="tall"><td>Bankkonforme<br>Verkaufsdokumentation</td><td>Kostenlos</td><td>Kostenlos</td></tr>
  </table>
  <p class="footnote">*Die Kosten der HBV-Schätzung werden vollumfänglich von der Erfolgsprovision in Abzug gebracht, sofern das Geschäft mit einem durch die Kranich Wohnbau GmbH nachgewiesenen Käufer abgeschlossen wird.</p>

  <div class="band-red band-red--five"></div>
  <div class="photo-cut" style="left:44px"><div class="photo photo-villa" role="img" aria-label="Foto eines mehrstöckigen Hauses mit Garten"></div></div>
  <div class="photo-cut" style="left:190px"><div class="photo photo-attic" role="img" aria-label="Foto eines hellen Dachzimmers mit Parkettboden"></div></div>
  <div class="photo-cut" style="left:339px"><div class="photo photo-living" role="img" aria-label="Foto eines Wohnraums mit Holzdecke, Pflanzen und Tonfliesen"></div></div>

  <div class="skyline" role="img" aria-label="Skizzierte graue Häusersilhouette"></div>
</section>

<div class="page-label page-label--four">Page 4</div>
<div class="page-label page-label--five">Page 5</div>

</body>
</html>
```